New Business Card Design Project

Use the flyer uploaded and website www.brightoakbuilders.com for inspiration.
List Our Services on Backside of business cards
Martin Hollis
Harborline Renovations Inc.
Licensed General Contractors
858-471-9063

Contact Information for Business Card

Use the flyer uploaded and website www.brightoakbuilders.com for inspiration. List Our Services on Backside of business cards Martin Hollis Harborline Renovations Inc. Licensed General Contractors 858-471-9063

```html
<!DOCTYPE html>
<html lang="en">
<head>
<meta charset="utf-8">
<title>Harborline Renovations – Business Card</title>
<link rel="stylesheet" href="https://fonts.googleapis.com/css2?family=Cinzel:wght@400;600&family=Poppins:wght@400;600&family=Roboto:wght@400&display=swap">
<style>
  :root {
    --bg: #2e2e2e;
    --card-black: #141414;
    --card-blue: #3581c6;
    --accent-red: #e3141b;
    --white: #ffffff;
  }
  * { box-sizing: border-box; margin: 0; padding: 0; }
  html, body { width: 1200px; height: 866px; overflow: hidden; }
  body {
    background: var(--bg);
    display: flex;
    flex-direction: column;
    align-items: center;
    justify-content: center;
    gap: 40px;
    font-family: "Roboto", sans-serif;
    color: var(--white);
  }
  .card {
    position: relative;
    width: 680px;
    height: 389px;
    background: var(--card-black);
    overflow: hidden;
    box-shadow: 0 10px 24px rgba(0,0,0,.45);
  }
  .card__shape { position: absolute; inset: 0; width: 100%; height: 100%; }
  .card__shape polygon { fill: var(--card-blue); }

  .brand {
    position: absolute;
    font-family: "Cinzel", serif;
    font-weight: 400;
    color: var(--white);
    letter-spacing: 3px;
    text-align: center;
    line-height: 1.15;
  }

  /* Front */
  .front__company {
    position: absolute;
    left: 34px; top: 30px;
    font-family: "Poppins", sans-serif;
    font-size: 18px;
    line-height: 1.3;
    color: var(--accent-red);
  }
  .front__name {
    position: absolute;
    left: 34px; top: 196px;
    font-family: "Cinzel", serif;
    font-weight: 600;
    font-size: 30px;
    letter-spacing: 2px;
  }
  .contact-list {
    position: absolute;
    left: 34px; top: 248px;
    list-style: none;
    font-size: 18px;
    line-height: 1.45;
  }
  .contact-list li { display: flex; align-items: center; gap: 10px; }
  .contact-list svg { width: 16px; height: 16px; fill: none; stroke: var(--white); stroke-width: 1.8; }
  .front .brand { right: 40px; top: 230px; font-size: 30px; width: 300px; }

  /* Back */
  .back .brand { right: 28px; top: 44px; font-size: 26px; width: 250px; }
  .services {
    position: absolute;
    left: 34px; top: 120px;
    font-family: "Poppins", sans-serif;
  }
  .services__heading { font-weight: 600; font-size: 18px; line-height: 1.2; }
  .services__sub { font-size: 15px; margin-bottom: 8px; }
  .services__columns { display: flex; gap: 26px; }
  .services__list { list-style: none; font-size: 15px; line-height: 1.45; }
  .services__list li::before { content: "• "; }
  .services__list--right { margin-top: 70px; }
</style>
</head>
<body>

<section class="card front" aria-label="Card front">
  <svg class="card__shape" viewBox="0 0 680 389" preserveAspectRatio="none" aria-hidden="true">
    <polygon points="0,389 0,120 100,100 410,389"/>
  </svg>
  <p class="front__company">Harborline Renovations Inc.<br>Licensed General Contractors</p>
  <h1 class="front__name">MARTIN HOLLIS</h1>
  <ul class="contact-list">
    <li><svg viewBox="0 0 16 16"><path d="M3 2l3 3-2 2c1 2 3 4 5 5l2-2 3 3-2 2C7 15 1 9 1 4z"/></svg>858-471-9063</li>
    <li><svg viewBox="0 0 16 16"><rect x="1" y="3" width="14" height="10"/><path d="M1 3l7 6 7-6"/></svg>info@harborlinereno.com</li>
    <li><svg viewBox="0 0 16 16"><circle cx="8" cy="8" r="7"/><path d="M1 8h14M8 1c3 3 3 11 0 14M8 1c-3 3-3 11 0 14"/></svg>www.brightoakbuilders.com</li>
  </ul>
  <p class="brand">Harborline Renovations</p>
</section>

<section class="card back" aria-label="Card back">
  <svg class="card__shape" viewBox="0 0 680 389" preserveAspectRatio="none" aria-hidden="true">
    <polygon points="0,0 190,0 680,340 680,389 0,389"/>
  </svg>
  <p class="brand">Harborline Renovations</p>
  <div class="services">
    <h2 class="services__heading">OUR SERVICES ARE 100%<br>GUARENTEED</h2>
    <p class="services__sub">SPECIALIZING IN</p>
    <div class="services__columns">
      <ul class="services__list">
        <li>Remodel: Kitchen &amp; Bath</li>
        <li>Painting: Interior &amp; Exterior</li>
        <li>Flooring: Carpet, Vinyl, Wood</li>
        <li>Window &amp; Door Replacement</li>
        <li>Plumbing: Repairs &amp; Upgrades</li>
      </ul>
      <ul class="services__list services__list--right">
        <li>Energy-Efficient Upgrades</li>
        <li>Deck &amp; Patio Construction</li>
        <li>Water &amp; Mold Damage</li>
        <li>Garage Renovation</li>
      </ul>
    </div>
  </div>
</section>

</body>
</html>
```